Advert for Services that we offer

Brenwick Torque Ltd need an design to represent what we do in a modern way by showing an image with a brief description and the use of corporate logo the information we will proved vie a doc file and this is to be presented in a modern way. This design will be for print & web. we have done our own design and its not great i have put this in the file repository

Target Market(s)

Motor trade

Font styles to use
Sans Serif

Colors

Designer to choose colors to be used in the design.

Requirements
Must have
• Company colour scheme as per logo within the files uploaded.
• and a small boarder to isolate it from the rest of the articles.
Nice to have
• Modern font
Should not have
• Old style font

```html
<!DOCTYPE html>
<html lang="en">
<head>
<meta charset="utf-8">
<title>Brenwick Torque Ltd – Product Testing &amp; Analysis</title>
<link rel="stylesheet" href="https://fonts.googleapis.com/css2?family=Exo+2:wght@500;600;700&family=Roboto:wght@400;500;700&display=swap">
<style>
  :root {
    --brand-blue: #2a7cc4;
    --frame-grey: #8a8d90;
    --ink-black: #050607;
    --text-white: #ffffff;
    --photo-dark: #1e2022;
    --photo-grey: #55585b;
    --photo-light: #8c8f92;
    --photo-red: #b4462a;
    --photo-skin: #b88a6e;
  }
  html, body {
    margin: 0;
    padding: 0;
    overflow: hidden;
    background: #ffffff;
  }
  .advert {
    position: relative;
    width: 1200px;
    height: 848px;
    box-sizing: border-box;
    border: 5px solid var(--brand-blue);
    background: var(--ink-black);
    overflow: hidden;
    font-family: "Roboto", Arial, sans-serif;
    color: var(--text-white);
  }
  .advert__photo {
    position: absolute;
    top: 0;
    right: 0;
    bottom: 0;
    width: 760px;
    background:
      radial-gradient(ellipse 150px 170px at 470px 640px, var(--photo-red) 0%, rgba(180,70,42,0.85) 45%, rgba(180,70,42,0) 75%),
      radial-gradient(ellipse 200px 220px at 470px 640px, var(--photo-light) 0%, rgba(140,143,146,0.5) 60%, rgba(140,143,146,0) 80%),
      radial-gradient(ellipse 130px 150px at 600px 170px, rgba(184,138,110,0.75) 0%, rgba(184,138,110,0) 75%),
      linear-gradient(100deg, rgba(0,0,0,0) 70%, var(--photo-grey) 71%, #3c3f42 100%),
      linear-gradient(180deg, #3a3c3e 0%, var(--photo-dark) 60%, #2a2c2e 100%);
    -webkit-mask-image: linear-gradient(90deg, rgba(0,0,0,0) 0%, rgba(0,0,0,0.55) 30%, #000 55%);
            mask-image: linear-gradient(90deg, rgba(0,0,0,0) 0%, rgba(0,0,0,0.55) 30%, #000 55%);
  }
  .advert__frame {
    position: absolute;
    left: 15px;
    top: 12px;
    right: 15px;
    bottom: 12px;
    border: 1px solid var(--frame-grey);
    pointer-events: none;
  }
  .brand {
    position: absolute;
    left: 60px;
    top: 150px;
    display: flex;
    align-items: center;
    gap: 14px;
  }
  .brand__square {
    width: 34px;
    height: 34px;
    background: var(--brand-blue);
  }
  .brand__name {
    margin: 0;
    font-family: "Exo 2", Arial, sans-serif;
    font-weight: 600;
    font-size: 38px;
    letter-spacing: 1px;
    color: var(--brand-blue);
    line-height: 1;
    white-space: nowrap;
  }
  .headline {
    position: absolute;
    left: 60px;
    top: 289px;
    margin: 0;
    font-family: "Exo 2", Arial, sans-serif;
    font-weight: 500;
    font-size: 43px;
    letter-spacing: 2.5px;
    line-height: 1;
    text-shadow: 0 2px 4px rgba(0,0,0,0.6);
    white-space: nowrap;
  }
  .services {
    position: absolute;
    left: 60px;
    top: 378px;
    margin: 0;
    padding: 0;
    list-style: none;
  }
  .services__item {
    position: relative;
    padding-left: 32px;
    height: 46.7px;
    font-size: 28px;
    letter-spacing: 1.2px;
    line-height: 30px;
    white-space: nowrap;
  }
  .services__item::before {
    content: "";
    position: absolute;
    left: 2px;
    top: 13px;
    width: 6px;
    height: 6px;
    border-radius: 50%;
    background: var(--brand-blue);
  }
  .contact-band {
    position: absolute;
    left: 0;
    top: 622px;
    width: 610px;
    height: 81px;
  }
  .contact-phone {
    position: absolute;
    left: 58px;
    top: 640px;
    margin: 0;
    font-weight: 700;
    font-size: 42px;
    letter-spacing: 2px;
    line-height: 1;
    white-space: nowrap;
  }
  .contact-web {
    position: absolute;
    left: 58px;
    top: 726px;
    margin: 0;
    font-size: 26px;
    letter-spacing: 0.3px;
    line-height: 1;
    white-space: nowrap;
  }
</style>
</head>
<body>
  <main class="advert">
    <div class="advert__photo" role="img" aria-label="Photograph of a technician in dark work overalls and safety glasses measuring the bore of a red cast wheel hub with a digital dial gauge in a workshop"></div>
    <div class="advert__frame"></div>

    <div class="brand">
      <span class="brand__square" aria-hidden="true"></span>
      <h1 class="brand__name">BRENWICK TORQUE LTD</h1>
    </div>

    <h2 class="headline">PRODUCT TESTING &amp; ANALYSIS</h2>

    <ul class="services">
      <li class="services__item">METALLURGICAL TESTING</li>
      <li class="services__item">BEARING PRE-LOAD TESTING</li>
      <li class="services__item">BORE MEASUREMENT</li>
      <li class="services__item">NEW PRODUCT EVALUATION</li>
      <li class="services__item">PRODUCT ANALYSIS &amp; REPORT</li>
    </ul>

    <svg class="contact-band" viewBox="0 0 610 81" aria-hidden="true">
      <polygon points="0,0 487,0 607,81 0,81" fill="var(--brand-blue)"/>
    </svg>
    <p class="contact-phone">TEL: 0161 555 0192</p>

    <p class="contact-web">WWW.BRENWICK-TORQUE.CO.UK</p>
  </main>
</body>
</html>
```